C2C website is looking for a web-designer

Complete description of the project you will find in the file atteched (we updated information there and maybe now it will be easier to understand what it's all about). We are a small team of two people from the Czech Republic and we want to create a united platform in the form of adverts, where people can find smb who will help them to cope with the everyday routine (cooking, cleaning, pet care, house work etc.)
Project Deadline Extended Reason: We want the designers to have more time for work. Added Wednesday, September 24, 2014
This brief depends on brief 402617 - http://gigs.pixelharbor-example.com/task.aspx?id=402617 (logo design). Both are for the same project. Added Wednesday, September 24, 2014
Industry/Entity Type
House
Number of Pages Required
5+ page
Look and feel
Each slider illustrates characteristics of the customer's brand and the style your logo design should communicate.

```html
<!DOCTYPE html>
<html lang="en">
<head>
<meta charset="utf-8">
<title>DomaPomoc.cz – Home</title>
<link href="https://fonts.googleapis.com/css2?family=Open+Sans:wght@400;600;700&family=Varela+Round&display=swap" rel="stylesheet">
<style>
:root{
  --green:#3aa019;
  --green-light:#6cc93a;
  --green-dark:#2f8a12;
  --ink:#222;
  --body:#777;
  --muted:#999;
  --line:#dcdcdc;
  --dark-bar:#444;
  --bg:#fff;
}
*{box-sizing:border-box;margin:0;padding:0}
html,body{width:839px;height:1200px;overflow:hidden;background:var(--bg)}
body{position:relative;font-family:"Open Sans",sans-serif;color:var(--ink)}
.abs{position:absolute}
.heading{font-family:"Varela Round",sans-serif}

.login-field{height:20px;border:1px solid var(--line);font-size:8px;color:#666;padding:5px 8px;top:13px}
.login-btn{left:526px;top:13px;width:46px;height:20px;background:#333;color:#fff;font-size:8.5px;text-align:center;line-height:20px}
.user-links{left:590px;top:13px;font-size:9.5px;color:#555}
.user-links span{margin:0 4px;color:#999}

.brand{left:84px;top:44px;font-family:"Varela Round",sans-serif;font-size:26px;color:var(--green)}
.search{left:323px;top:50px;width:246px;height:27px;border:1px solid var(--line);border-radius:3px;font-size:8.5px;color:#888;padding:7px 10px}
.search svg{position:absolute;right:7px;top:5px}

.nav{left:80px;top:90px;width:683px;height:35px;background:linear-gradient(#6fcb3b,#3fa01c);display:flex}
.nav a{font-family:"Varela Round",sans-serif;color:#fff;font-size:13px;text-decoration:none;padding:0 13px;line-height:35px;border-right:1px solid rgba(0,0,0,.15)}
.nav a:last-child{border:none}

.hero{left:80px;top:125px;width:685px;height:325px;background:linear-gradient(100deg,#6d6560 0%,#8a7b70 40%,#c9bfb6 70%,#e8e2db 100%)}
.crumb{left:80px;top:125px;width:683px;height:21px;background:rgba(60,60,60,.85);color:#fff;font-size:9px;padding:4px 19px}
.caption{left:118px;top:212px;width:217px;height:179px;background:rgba(60,60,60,.85);color:#fff;padding:22px 21px}
.caption h1{font-family:"Varela Round",sans-serif;font-weight:400;font-size:24px}
.caption h2{font-family:"Varela Round",sans-serif;font-weight:400;font-size:15px;margin-top:2px}
.caption p{font-size:9px;line-height:16px;margin-top:8px}
.dots{display:flex;gap:4px;margin-top:10px}
.dots i{width:8px;height:8px;border-radius:50%;background:#ddd}

.section-title{left:80px;top:475px;font-family:"Varela Round",sans-serif;font-size:19px}
.section-title em{font-style:normal;color:var(--green)}

.post{left:82px;width:460px}
.post-thumb{position:absolute;left:0;top:0;width:133px;height:80px;background:linear-gradient(135deg,#c9b8a8,#8e9bb0)}
.post-body{position:absolute;left:143px;top:0;width:315px}
.post-body h3{font-family:"Varela Round",sans-serif;font-weight:400;font-size:11.5px;margin-bottom:5px}
.post-body p{font-size:8.6px;line-height:14.6px;color:var(--body)}
.post-links{font-size:10px;color:var(--green);margin-top:5px}
.post-links span{color:var(--ink);margin:0 4px}

.box{border:1px solid var(--line);border-radius:3px;background:linear-gradient(#fff 80%,#f4f4f4)}
.featured{left:563px;top:474px;width:202px;height:249px}
.featured h4{font-family:"Varela Round",sans-serif;font-weight:400;font-size:14.5px;padding:13px 18px 8px;border-bottom:1px solid var(--line)}
.feat{position:absolute;left:16px;width:180px}
.feat-thumb{position:absolute;left:0;top:0;width:56px;height:48px;background:linear-gradient(135deg,#b9a89a,#6e86a8)}
.feat-text{position:absolute;left:64px;top:0;width:116px}
.feat-text b{display:block;font-weight:400;font-size:9.5px;margin-bottom:2px}
.feat-text p{font-size:7px;line-height:12px;color:var(--muted)}

.newsletter{left:563px;top:732px;width:202px;height:148px;padding:15px 17px}
.newsletter h4{font-family:"Varela Round",sans-serif;font-weight:400;font-size:15px;color:var(--green)}
.newsletter p{font-size:8.5px;color:var(--muted);margin-top:2px}
.nl-field{width:168px;height:21px;border:1px solid var(--line);border-radius:2px;font-size:8px;color:#777;padding:5px 9px;margin-top:8px}
.subscribe{display:inline-block;margin-top:6px;background:var(--green);color:#fff;font-size:10px;font-weight:600;padding:5px 13px;border-radius:2px}

.ad{left:559px;top:895px;width:207px;height:172px;background:linear-gradient(90deg,#1f2f6b 0%,#2a3c82 65%,#c8ccd8 100%);border:1px solid #aaa}

.footer-rule{left:0;top:1117px;width:839px;height:1px;background:var(--line)}
.footer-nav{left:90px;top:1139px;font-size:11px;color:var(--ink)}
.footer-nav span{margin:0 4px}
.copy{left:90px;top:1163px;font-size:8.5px;color:#444}
.social{left:696px;top:1142px;display:flex;gap:6px}
.social i{width:15px;height:15px;background:#3b5b99;display:block}
.social i:nth-child(2){background:#4cb3e6}
.social i:nth-child(3){background:#1d6fa5}
</style>
</head>
<body>

<div class="abs login-field" style="left:342px;width:89px">Username</div>
<div class="abs login-field" style="left:435px;width:89px">Password</div>
<div class="abs login-btn">Login</div>
<div class="abs user-links">My profile<span>|</span>My messages<span>|</span>Statistics</div>

<div class="abs brand">DomaPomoc.cz</div>
<div class="abs search">type your word
  <svg width="17" height="17" viewBox="0 0 17 17"><circle cx="7" cy="7" r="5.5" fill="none" stroke="#aaa" stroke-width="1.6"/><line x1="11" y1="11" x2="15.5" y2="15.5" stroke="#aaa" stroke-width="1.8"/></svg>
</div>

<nav class="abs nav">
  <a>Discussion</a><a>Articles</a><a>Users</a><a>Registration</a><a>Advertisments</a><a>Support</a><a>Blog</a>
</nav>

<div class="abs hero" role="img" aria-label="Smiling woman stirring a pot with a wooden spoon in a home kitchen"></div>
<div class="abs crumb">home ›</div>
<div class="abs caption">
  <h1>Cooking Service</h1>
  <h2>Nulla sit amet diam</h2>
  <p>Vivamus porttitor purus nisi eleifend libero a tempus libero lectus feugiat felis Morbi diam mauris viver</p>
  <div class="dots"><i></i><i></i><i></i><i></i></div>
</div>

<div class="abs section-title">Recent <em>Discussion</em></div>

<article class="abs post" style="top:513px">
  <div class="post-thumb" role="img" aria-label="Young carer helping an elderly woman at the table"></div>
  <div class="post-body">
    <h3>Ut nisi erat fermentum vel congue</h3>
    <p>Etiam est nunc venenatis in tristique eu imperdiet ac nisl Cum sociis natoque penatibus et magnis dis parturient montes nascetur ridiculus mus In iaculis facilisis massa Etiam eu urna Sed porta Suspendisse quam leo molestie sed luctus quis feugiat in pede Fusce tellus Sed metus augue convalli</p>
    <div class="post-links">Read More<span>|</span>Comments</div>
  </div>
</article>

<article class="abs post" style="top:633px">
  <div class="post-thumb" role="img" aria-label="Nanny playing with children and toy blocks"></div>
  <div class="post-body">
    <h3>Nunc porta convallis pede</h3>
    <p>Etiam est nunc venenatis in tristique eu imperdiet ac nisl Cum sociis natoque penatibus et magnis dis parturient montes nascetur ridiculus mus In iaculis facilisis massa Etiam eu urna Sed porta Suspendisse quam leo molestie sed luctus quis feugiat in pede Fusce tellus Sed metus augue convalli</p>
    <div class="post-links">Read More<span>|</span>Comments</div>
  </div>
</article>

<article class="abs post" style="top:751px">
  <div class="post-thumb" role="img" aria-label="Woman in blue sweater cleaning a kitchen"></div>
  <div class="post-body">
    <h3>Curabitur vel mi sit amet magna</h3>
    <p>Etiam est nunc venenatis in tristique eu imperdiet ac nisl Cum sociis natoque penatibus et magnis dis parturient montes nascetur ridiculus mus In iaculis facilisis massa Etiam eu urna Sed porta Suspendisse quam leo molestie sed luctus quis feugiat in pede Fusce tellus Sed metus augue convalli Morbi ornare gravida elit Integer congue augue et malesuada iaculis ipsum dui aliquet felis at cursus magna nisl nec elit Praesent elementum elit at tellus nec ultricies sit amet porttitor mattis enim In massa</p>
    <div class="post-links">Read More<span>|</span>Comments</div>
  </div>
</article>

<article class="abs post" style="top:912px">
  <div class="post-thumb" role="img" aria-label="Woman with cleaning supplies in a bright kitchen"></div>
  <div class="post-body">
    <h3>Morbi porta libero id ullamcorper</h3>
    <p>Mauris vel lacus vitae felis vestibulum volutpat Etiam est nunc venenatis in tristique eu imperdiet ac nisl Cum sociis natoque penatibus et magnis dis parturient montes nascetur ridiculus mus In iaculis facilisis massa Etiam eu urna Sed porta Suspendisse quam leo molestie sed luctus quis feugiat in pede Fusce tellus Sed metus augue convallis et vehicula</p>
    <div class="post-links">Read More<span>|</span>Comments</div>
  </div>
</article>

<aside class="abs box featured">
  <h4>Featured Service</h4>
  <div class="feat" style="top:47px">
    <div class="feat-thumb" role="img" aria-label="Babysitter with a toddler"></div>
    <div class="feat-text"><b>Etiam est nunc venenatis</b><p>Integer orci tellus tristique vitae consequat nec porta vel lectus Nulla sit amet diam Dui</p></div>
  </div>
  <div class="feat" style="top:109px">
    <div class="feat-thumb" role="img" aria-label="Handyman at a front door"></div>
    <div class="feat-text"><b>Fusce ultricies</b><p>Integer orci tellus tristique vitae consequat nec porta vel lectus Nulla sit amet diam Dui</p></div>
  </div>
  <div class="feat" style="top:170px">
    <div class="feat-thumb" role="img" aria-label="Woman ironing laundry"></div>
    <div class="feat-text"><b>Ut nisi fermentum</b><p>Integer orci tellus tristique vitae consequat nec porta vel lectus Nulla sit amet diam Dui</p></div>
  </div>
</aside>

<aside class="abs box newsletter">
  <h4>Newsletters Sign Up</h4>
  <p>Please Sign up here for latest offers.</p>
  <div class="nl-field">Your Name</div>
  <div class="nl-field">Email address</div>
  <div class="subscribe">SUBSCRIBE</div>
</aside>

<div class="abs ad" role="img" aria-label="Banner advertisement for sports trading cards with newspaper coupons"></div>

<div class="abs footer-rule"></div>
<div class="abs footer-nav">Home<span>|</span>Articles<span>|</span>Discussion<span>|</span>Services<span>|</span>Advertisments<span>|</span>Contact</div>
<div class="abs copy">© 2014 Company Name &nbsp;All right reserved &nbsp;Term of Use</div>
<div class="abs social" aria-label="Social links"><i></i><i></i><i></i></div>

</body>
</html>
```